Web Design Project for Industrial Hemp

I'm launching a new company to grow Industrial Hemp and then to set up a manufacturing facility to process the crop each and every year. We require a complete end to end brand and livery suite and we will start with a web presence. We want to appeal to (a) Investors, Employees, Farmers, and consumers so as to engage with all our stakeholders. We want to create a whole new industry that becomes a game changer for environmentally friendly crop production. Hemp is gaining in popularity and credibility across the world!

Target Market(s)

Farmers to produce, Manufacturers who will purchase the raw materials, Investors who will invest in the project, Consumers who will buy Hemp Products

Industry/Entity Type

Industry

Requirements
Must have
• Environmentally Friendly
Carbon Neutral/Positive
Game Changer
Multi-Use Crop
50,000 products can be made from Hemp
Should not have
• Should avoid its relationship with cannabis but not ignore it! When the regulatory bodies acknowledge the benefits of cannabanoids, they will start to legalise the production of cannabis for sale on prescription

```html
<!DOCTYPE html>
<html lang="en">
<head>
<meta charset="utf-8">
<title>Greenrow Hemp Works</title>
<link rel="stylesheet" href="https://fonts.googleapis.com/css2?family=Oswald:wght@300;400&family=Passion+One:wght@400;700&family=Anton&display=swap">
<style>
:root{
  --lime:#cfe3a0;
  --green:#2f8a10;
  --green-dark:#1f6a08;
  --olive:#6a9a1a;
  --leaf:#7ab52a;
  --gold:#c9ae57;
  --gold-dark:#8a6e1c;
  --cream:#eeede8;
  --footer:#e7e4d8;
  --text:#333;
  --grey:#555;
}
*{box-sizing:border-box;margin:0;padding:0}
html,body{width:784px;height:1200px;overflow:hidden}
body{background:var(--cream);font-family:Arial,Helvetica,sans-serif;color:var(--text);position:relative}
.header{position:absolute;left:0;top:0;width:784px;height:76px;background:var(--lime);border-bottom:4px solid var(--green)}
.brand{position:absolute;left:24px;top:46px;display:flex;align-items:center;gap:6px;background:var(--green);color:#fff;font-family:'Oswald',sans-serif;font-size:11px;letter-spacing:.5px;padding:2px 8px;white-space:nowrap}
.brand-mark{width:10px;height:10px;border-radius:50%;background:var(--lime)}
.search{position:absolute;left:592px;top:8px;width:177px;height:28px;background:#bcd88a;border-radius:6px;font-size:10px;color:var(--green-dark);padding:8px 0 0 13px}
.search-btn{position:absolute;right:4px;top:4px;width:24px;height:20px;background:var(--green);border-radius:4px}
.nav{position:absolute;top:0;left:0;width:784px;height:76px;font-family:'Oswald',sans-serif;font-weight:300;font-size:16px;color:var(--green-dark)}
.nav span{position:absolute;top:46px;white-space:nowrap;line-height:20px;transform:scaleX(.8);transform-origin:left}
.hero{position:absolute;left:0;top:80px;width:784px;height:358px;background:linear-gradient(180deg,#6e9a2e 0%,#5a8a22 40%,#7aa83a 70%,#4f7d1c 100%)}
.tiles{position:absolute;left:9px;top:51px;display:flex;gap:0}
.tile{width:128px;height:168px;background:rgba(40,80,10,.55);border-right:1px solid rgba(255,255,255,.15);padding:7px}
.tile-img{width:112px;height:112px}
.tile-label{font-family:'Oswald',sans-serif;color:#fff;font-size:24px;text-align:center;margin-top:8px;letter-spacing:.5px;white-space:nowrap}
.hero-title{position:absolute;left:0;width:784px;top:265px;text-align:center;color:#fff;font-family:'Anton',sans-serif;text-shadow:0 2px 3px rgba(0,0,0,.5);white-space:nowrap}
.hero-title b{font-size:42px;font-weight:400}
.hero-title i{font-family:'Passion One',sans-serif;font-style:normal;font-size:30px;font-weight:700}
.features{position:absolute;top:438px;left:0;width:784px;height:177px;border-bottom:1px solid #c8c8c0}
.feature{position:absolute;top:30px;width:185px}
.h{font-family:'Passion One',sans-serif;color:var(--olive);font-size:15px;font-weight:400;letter-spacing:.2px;text-transform:uppercase;white-space:nowrap}
.feature p{font-size:9.6px;line-height:11.5px;color:var(--grey);margin-top:10px}
.feature .ico{float:left;width:36px;height:36px;margin:2px 8px 0 4px}
.welcome{position:absolute;left:21px;top:648px;width:315px}
.photo{width:310px;height:152px;margin-top:14px;border:3px solid #fff;box-shadow:0 0 0 1px #ccc;background:linear-gradient(180deg,#4a86c6 0%,#a9c8e6 40%,#4d6f8a 52%,#9a6a30 70%,#6a4a20 100%)}
.welcome p{font-size:9.6px;line-height:11.6px;margin-top:9px}
.services{position:absolute;left:375px;top:648px}
.services ul{list-style:none;margin-top:12px}
.services li{font-size:9.8px;height:24px;padding-left:18px;position:relative;white-space:nowrap}
.services li:before{content:'»';position:absolute;left:3px;top:-4px;font-size:14px;color:#555}
.news{position:absolute;left:588px;top:648px;width:185px}
.news-item{position:relative;height:88px;border-bottom:1px dotted var(--gold);margin-top:12px;padding-left:44px}
.date{position:absolute;left:0;top:0;width:30px;text-align:center}
.date .d{width:26px;height:26px;margin:0 auto;border-radius:50%;background:var(--olive);border:2px solid var(--gold);color:#fff;font-family:'Oswald',sans-serif;font-size:13px;line-height:22px}
.date .m{font-size:10px;color:var(--gold-dark);margin-top:7px;letter-spacing:.5px}
.news-item h4{font-size:10px;color:#333;white-space:nowrap}
.news-item p{font-size:8.4px;color:#666;margin-top:5px;line-height:10.5px}
.news-item a{font-size:8.4px;color:var(--olive);font-weight:bold;display:block;margin-top:2px}
.more{margin-top:20px;display:inline-block;background:var(--gold);color:#fff;border:2px solid #e5d59a;border-radius:4px;font-family:'Passion One',sans-serif;font-size:14px;padding:2px 5px;white-space:nowrap}
.footer{position:absolute;top:962px;left:0;width:784px;height:238px;background:var(--footer)}
.fh{font-family:'Passion One',sans-serif;color:var(--gold-dark);font-size:16px;font-weight:400;position:absolute;top:14px;white-space:nowrap}
.fnav{position:absolute;left:26px;top:46px;display:grid;grid-template-columns:75px 80px;row-gap:3px;font-size:9.8px;color:var(--gold-dark)}
.field{position:absolute;left:273px;width:196px;background:#dcd8c8;border-radius:8px;font-size:8.8px;font-weight:bold;color:#5a4a18;padding:7px 0 0 17px}
.send{position:absolute;left:415px;top:176px;width:55px;height:23px;background:var(--gold);color:#5a4a18;font-size:10px;font-weight:bold;text-align:center;line-height:23px;border-radius:2px}
.social{position:absolute;left:596px;top:47px;display:flex;gap:6px}
.social span{width:23px;height:23px;border-radius:50%;background:var(--gold)}
.sub{position:absolute;left:596px;top:82px;font-size:8.8px;color:#5a4a18;line-height:11px}
.sub-input{position:absolute;left:595px;top:108px;width:148px;height:20px;border-radius:10px;background:var(--gold);color:#fff;font-size:8.5px;padding:5px 12px}
.sub-link{position:absolute;left:598px;top:138px;font-size:8.8px;font-weight:bold;color:#5a4a18}
.phone{position:absolute;left:594px;top:165px;display:flex;align-items:center;gap:8px;font-family:'Oswald',sans-serif;font-weight:300;color:var(--gold);font-size:21px;white-space:nowrap}
</style>
</head>
<body>
<header class="header">
  <div class="brand"><span class="brand-mark"></span>GREENROW HEMP WORKS</div>
  <div class="search">SEARCH<div class="search-btn"></div></div>
  <nav class="nav">
    <span style="left:257px">HOME</span>
    <span style="left:322px">ABOUT US</span>
    <span style="left:410px">PRODUCTION</span>
    <span style="left:515px">INVESTORS</span>
    <span style="left:608px">PRODUCTS</span>
    <span style="left:702px">CONTACT US</span>
  </nav>
</header>

<section class="hero" role="img" aria-label="Field of green hemp plants">
  <div class="tiles">
    <div class="tile"><div class="tile-img" role="img" aria-label="Bowl of hemp granola" style="background:linear-gradient(#f3eee4,#c99a5a)"></div><div class="tile-label">FOOD</div></div>
    <div class="tile"><div class="tile-img" role="img" aria-label="Fuel pump nozzle" style="background:linear-gradient(135deg,#e8e0d8,#3b4a8a)"></div><div class="tile-label">FUEL</div></div>
    <div class="tile"><div class="tile-img" role="img" aria-label="Bundle of raw fibre" style="background:linear-gradient(#c8c4a8,#7a7460)"></div><div class="tile-label">FIBER</div></div>
    <div class="tile"><div class="tile-img" role="img" aria-label="Amber oil in a pan" style="background:radial-gradient(circle at 45% 55%,#c0601a,#3a2a18)"></div><div class="tile-label">OIL</div></div>
    <div class="tile"><div class="tile-img" role="img" aria-label="Sheet of hemp paper" style="background:linear-gradient(#e0d2a8,#cdb886)"></div><div class="tile-label">PAPER</div></div>
    <div class="tile"><div class="tile-img" role="img" aria-label="Folded hemp textile" style="background:linear-gradient(#e8e8e6,#7a7a78)"></div><div class="tile-label">TEXTILES</div></div>
  </div>
  <div class="hero-title"><b>50,000 PRODUCTS</b> <i>CAN BE MADE FROM HEMP</i></div>
</section>

<section class="features">
  <div class="feature" style="left:14px">
    <h3 class="h">Environmental Friendly</h3>
    <p><svg class="ico" viewBox="0 0 36 36"><path d="M18 32V18" stroke="var(--leaf)" stroke-width="2"/><path d="M18 20C10 20 6 14 6 8c8 0 12 5 12 12zM18 18c0-8 5-12 13-12 0 7-5 12-13 12z" fill="var(--leaf)"/><path d="M6 32h24" stroke="var(--leaf)" stroke-width="2"/></svg>Donec hendrerit, felis in aliquet sodales, leo neque posuere arcu, sit amet sodales libero augue eget libero. Proin consequat odio eget ligula lobortis sodales. Suspendisse potenti.</p>
  </div>
  <div class="feature" style="left:212px">
    <h3 class="h">Carbon Neutral Positive</h3>
    <p><span class="ico" style="font-family:'Oswald',sans-serif;color:var(--leaf);font-size:24px;width:42px;line-height:30px">CO<sup style="font-size:11px">2</sup></span>Vntur magni dolores eoquie voluptate msequi nesciunt. Nique porroisquam esti dolorem ipsumquia dolorsita onsectet. Ferpisci velit, sed quia non numquam eiumodi tempora.</p>
  </div>
  <div class="feature" style="left:404px">
    <h3 class="h">Game Changer</h3>
    <p><svg class="ico" viewBox="0 0 36 36"><rect x="4" y="22" width="5" height="10" fill="var(--leaf)"/><rect x="12" y="18" width="5" height="14" fill="var(--leaf)"/><rect x="20" y="20" width="5" height="12" fill="var(--leaf)"/><path d="M3 20l9-8 6 5 12-11" stroke="var(--leaf)" stroke-width="2.5" fill="none"/><path d="M26 5h6v6z" fill="var(--leaf)"/></svg>Aenean placerat tortor ac dui luctus ut mattis est mollis. Donec blandit orci id velit cursus varius. Fusce quam ultrices a, vestibulum nec enim. Quisque imperdiet ultricies dolor in convallis.</p>
  </div>
  <div class="feature" style="left:592px">
    <h3 class="h">Multi-User Crop</h3>
    <p><svg class="ico" viewBox="0 0 36 36"><rect x="6" y="4" width="16" height="14" fill="none" stroke="var(--leaf)" stroke-width="2"/><path d="M10 14l4-5 4 5z" fill="var(--leaf)"/><path d="M14 22c6 0 10 4 16 8H6c2-4 4-8 8-8z" fill="var(--leaf)"/></svg>Donec hendrerit, felis in aliquet sodales, leo neque posuere arcu, sit amet sodales libero augue eget libero. Proin consequat odio eget ligula lobortis sodales. Suspendisse potenti.</p>
  </div>
</section>

<section class="welcome">
  <h2 class="h">Welcome to Greenrow Hemp Works</h2>
  <div class="photo" role="img" aria-label="Coastal landscape with hills and bay"></div>
  <p>Jerta baditaut onquser kaytsrera untur magni dolores eoquie voluptate msequi nesciunt. Nique porroisquam esti dolorem ipsumquia dolorsitamet consectet rpisci velit.Bahseoquie voluptate msequisagni dolores nesciunt. Nique porrisquam estqui dolorem ipsumquia dolor adipisci unumquam labore esitamet consect olore nuaysas.</p>
</section>

<section class="services">
  <h2 class="h">Products and Services</h2>
  <ul>
    <li>Lorem ipsum dolor sit amet</li>
    <li>Consectetur adipisicing elit</li>
    <li>Sed do eiusmod tempor</li>
    <li>Incididunt ut labore et dolore</li>
    <li>Magna aliqua. Ut enim ad</li>
    <li>Minim veniam, quis nostrud</li>
    <li>Exercitation ullamco laboris</li>
    <li>Nisi ut aliquip ex ea commodo</li>
  </ul>
</section>

<section class="news">
  <h2 class="h">Latest News</h2>
  <div class="news-item">
    <div class="date"><div class="d">27</div><div class="m">JULY</div></div>
    <h4>Lorem ipsum dolor sit amet</h4>
    <p>Lorem ipsum dolor sit amet, consectetur adipisicing elit, sed do.</p>
    <a>read more +</a>
  </div>
  <div class="news-item">
    <div class="date"><div class="d">26</div><div class="m">JUNE</div></div>
    <h4>Sed ut perspiciatis, unde</h4>
    <p>Sed ut perspiciatis, unde omnis iste natus error sit voluptatem accusan</p>
    <a>read more +</a>
  </div>
  <span class="more">MORE NEWS</span>
</section>

<footer class="footer">
  <h2 class="fh" style="left:26px">NAVIGATION</h2>
  <div class="fnav"><span>Home</span><span>Sitemap</span><span>About Us</span><span>Contact Us</span><span>Production</span><span>Terms of Use</span><span>Investors</span><span></span><span>Products</span></div>

  <h2 class="fh" style="left:278px">EMAIL US</h2>
  <div class="field" style="top:47px;height:23px">full name</div>
  <div class="field" style="top:72px;height:23px">email address</div>
  <div class="field" style="top:98px;height:71px"></div>
  <div class="send">send</div>

  <h2 class="fh" style="left:597px">CONTACT US</h2>
  <div class="social"><span></span><span></span><span></span><span></span><span></span></div>
  <p class="sub">subscribe to our monthly newsletter<br>and get the best deals and discounts</p>
  <div class="sub-input">enter email address</div>
  <div class="sub-link">➤ &nbsp;subscribe now</div>
  <div class="phone"><svg width="22" height="22" viewBox="0 0 22 22"><circle cx="11" cy="11" r="10" fill="none" stroke="var(--gold)" stroke-width="1.5"/><path d="M7 6c1-1 2 0 3 2s-1 2 0 3 1 2 3 2 2 2 1 3-5 0-7-3-1-6 0-7z" fill="var(--gold)"/></svg>0-98-7654321</div>
</footer>
</body>
</html>
```